Play Equipment Distributor Website

We need a design (no coding) of a website for our play equipment sales company. The website will be in Japanese and is targeted at the Japanese market, and as such should be designed with that in mind.
The website will have 5 sections: home/top, products, safety, company information, contact. Initially we would like to have the top and Pebble Climb Works (our main product) pages designed. The main call to action - Request Catalog - should be present on all pages. The copy is still in the making, so please use Japanese dummy text to fill the pages for now.
For inspiration regarding the design, this is a website that we like very much: http://www.yardloopgear.example/
Attaching our logo, other graphics, as well as a rough idea of what we have on our mind in terms of layout and content of each page.
Target Market(s)
Japanese playset users - kindergartens, schools, entertainment parks, etc.

```html
<!DOCTYPE html>
<html lang="ja">
<head>
<meta charset="utf-8">
<title>Pebble Climb Works</title>
<link href="https://fonts.googleapis.com/css2?family=Noto+Sans+JP:wght@300;400;500;700&display=swap" rel="stylesheet">
<style>
:root{
  --orange:#f26b1d;
  --teal:#1dc6a4;
  --purple:#9a2fc4;
  --pink:#ee3f86;
  --green:#8cc63f;
  --brown:#5a3414;
  --yellow:#ffe21a;
  --field:#fff0a0;
  --white:#ffffff;
  --ink:#555555;
}
*{box-sizing:border-box;margin:0;padding:0}
html,body{width:1200px;height:4255px;overflow:hidden}
body{position:relative;font-family:"Noto Sans JP",sans-serif;background:var(--white);color:var(--ink)}
.abs{position:absolute}
.fill{position:absolute}
.btn{position:absolute;display:flex;align-items:center;justify-content:center;color:var(--white);font-size:19px;font-weight:500}
.btn-catalog{background:var(--purple);width:240px;height:54px}

/* header */
.hero{position:absolute;left:0;top:0;width:1200px;height:800px;background:linear-gradient(180deg,#4a8fd6 0%,#9cc6ea 28%,#6f9a4a 52%,#5f9a2e 75%,#7db33a 100%)}
.brand{position:absolute;left:28px;top:40px;display:flex;align-items:center;gap:12px;font-size:24px;font-weight:700;color:var(--white)}
.brand .dot{width:36px;height:36px;border-radius:50%;background:var(--white)}
.nav{position:absolute;top:62px;height:58px;display:flex;align-items:center;justify-content:center;color:var(--white);font-size:20px}
.hero-kicker{position:absolute;left:600px;width:560px;top:190px;text-align:center;font-size:32px;color:var(--orange);font-weight:500}
.hero-title{position:absolute;left:560px;width:640px;top:250px;text-align:center;font-size:54px;color:var(--orange);font-weight:400}

/* play intro */
.intro-title{position:absolute;left:120px;top:995px;font-size:46px;color:var(--green)}
.intro-title .o{color:var(--orange)}
.intro-text{position:absolute;left:124px;top:1082px;width:620px;font-size:14px;line-height:1.9}

/* teal */
.teal-title{position:absolute;left:0;width:1200px;top:1350px;text-align:center;color:var(--white);font-size:44px;font-weight:400}
.teal-text{position:absolute;left:52px;top:1468px;width:1096px;color:var(--white);font-size:14px;line-height:1.9;font-weight:500}
.thumb{position:absolute;top:1555px;height:168px}
.thumb-label{position:absolute;top:1735px;width:250px;text-align:center;color:var(--white);font-size:14px}
.value-line{position:absolute;left:0;width:1200px;text-align:center;color:var(--white);font-size:44px}

/* products */
.band{position:absolute;left:0;top:2133px;width:1200px;height:94px;background:var(--purple);display:flex;align-items:center;justify-content:center;color:var(--white);font-size:44px}
.prod-title{position:absolute;font-size:38px}
.prod-text{position:absolute;font-size:14px;line-height:1.9}
.mini-label{position:absolute;top:3558px;width:300px;text-align:center;font-size:30px}

/* footer */
.field{position:absolute;left:432px;width:340px;background:var(--field);font-size:14px;color:#8a7a3a;padding:6px 10px}
.social{position:absolute;left:374px;width:40px;height:40px;border-radius:50%;background:var(--white)}
.contact{position:absolute;left:896px;top:3940px;color:var(--white);font-size:15px;line-height:1.45}
.copy{position:absolute;left:0;top:4202px;width:1200px;text-align:center;color:var(--white);font-size:14px}
</style>
</head>
<body>

<!-- HERO -->
<section class="hero" role="img" aria-label="緑の芝生に置かれた木製ブランコセットで遊ぶ子どもたち"></section>
<div class="brand"><span class="dot"></span>Pebble Climb Works</div>
<nav>
  <div class="nav" style="left:363px;width:92px;background:var(--orange)">ホーム</div>
  <div class="nav" style="left:477px;width:142px;background:var(--teal)">プロダクト</div>
  <div class="nav" style="left:641px;width:92px;background:var(--pink)">安全性</div>
  <div class="nav" style="left:760px;width:194px;background:var(--green)">私たちに関しては</div>
  <div class="nav" style="left:976px;width:160px;background:var(--purple)">お問い合わせ</div>
</nav>
<p class="hero-kicker">見ブ青由運や球達う一つむ縫</p>
<h1 class="hero-title">自要ハア署表さへ無索ソウ</h1>
<a class="btn btn-catalog" style="left:894px;top:632px">オーダーカタログ</a>

<!-- PLAY INTRO -->
<section class="fill" style="left:0;top:800px;width:1200px;height:491px;background:linear-gradient(90deg,#ffffff 0%,#f4f4f4 100%)"></section>
<div class="fill" role="img" aria-label="黄色いテントブランコに座る子ども" style="left:760px;top:822px;width:440px;height:430px;background:linear-gradient(135deg,#f3f3f3 0%,#ffe433 45%,#f4c400 70%,#8a5a2a 100%)"></div>
<h2 class="intro-title">プレー<span class="o">の</span>重要性</h2>
<p class="intro-text">習をわん見ブ青由運や球達う一つむ縫2台要ハア署表さへ無索ソリ認職寿ネソ化議稿ミし端点ムワク図偶提チヨ出部ワレホテ所際長イ点ヌツモ浩品員ルイ天外62郷社も義警キロハワ幕景緑テチ全分ぴも図ぶ責し導争じ属テモ未期ネ外休ず図体ふ副見わまし報見ブノ宴業さう線文木ミニモ千16図とどべ続化文個職遺れへ。</p>

<!-- TEAL + ORANGE WAVE -->
<svg class="abs" style="left:0;top:1291px" width="1200" height="842" viewBox="0 0 1200 842" aria-hidden="true">
  <rect x="0" y="0" width="1200" height="842" fill="var(--teal)"/>
  <path d="M0 520 C180 470 300 500 420 530 C560 565 700 520 860 500 C1000 480 1100 470 1200 460 L1200 842 L0 842 Z" fill="var(--orange)"/>
</svg>
<h2 class="teal-title">プレーの重要性</h2>
<p class="teal-text">習をわん見ブ青由運や球達う一つむ縫2台要ハア署表さへ無索ソリ認職寿ネソ化議稿ミし端点ムワク図偶提チヨ出部ワレホテ所際長イ点ヌツモ浩品員ルイ天外62郷社も義警キロハワ幕景緑テチ全分ぴも図ぶ責し導争じ属テモ未期ネ外休ず図体ふ副見わまし報見ブノ宴業さう線文木ミニモ千16図とどべ続化文個職遺れへ。</p>
<div class="thumb" role="img" aria-label="赤いチューブ滑り台で遊ぶ子ども" style="left:57px;width:250px;background:linear-gradient(135deg,#2a2a2a,#c8303a 55%,#e8e0d8)"></div>
<div class="thumb" role="img" aria-label="丸窓からのぞく子ども" style="left:336px;width:254px;background:linear-gradient(135deg,#7a4a22,#e7b04a 50%,#5a3414)"></div>
<div class="thumb" role="img" aria-label="黄色いパネルのある木製遊具" style="left:616px;width:252px;background:linear-gradient(135deg,#6a8a40,#b88040 50%,#f0d020)"></div>
<div class="thumb" role="img" aria-label="黄色い遊具の横に立つ子ども" style="left:891px;width:250px;background:linear-gradient(135deg,#7aa8d8,#f0d020 50%,#5f8a30)"></div>
<p class="thumb-label" style="left:57px">習をわん見ブ青</p>
<p class="thumb-label" style="left:338px">習をわん見ブ青</p>
<p class="thumb-label" style="left:617px">習をわん見ブ青</p>
<p class="thumb-label" style="left:891px">習をわん見ブ青</p>
<p class="value-line" style="top:1812px">楽しさと手頃な価格の遊具を</p>
<p class="value-line" style="top:1878px">提供府プレイ赤字を解決!</p>
<a class="btn btn-catalog" style="left:480px;top:2008px">オーダーカタログ</a>

<!-- PRODUCTS -->
<div class="band">当社の製品</div>

<div class="fill" style="left:0;top:2227px;width:600px;height:511px;background:var(--orange)"></div>
<div class="fill" role="img" aria-label="黄色い滑り台と屋根付きタワーの木製遊具" style="left:600px;top:2240px;width:600px;height:490px;background:linear-gradient(160deg,#ffffff 0%,#e0b070 35%,#a0652a 60%,#f2d020 85%,#ffffff 100%)"></div>
<h3 class="prod-title" style="left:215px;top:2288px;color:var(--purple)">習をわん見</h3>
<p class="prod-text" style="left:30px;top:2382px;width:545px;color:var(--purple)">習をわん見ブ青由運や球達う一つむ縫2台要ハア署表さへ無索ソリ認職寿ネソ化議稿ミし端点ムワク図偶提チヨ出部ワレホテ所際長イ点ヌツモ浩品員ルイ天外62郷社も義警キロハワ幕景緑テチ全分ぴも図ぶ責し導争じ属テモ未期ネ外休ず図体ふ副見わまし報見ブノ宴業さう線文木ミニモ千16図とどべ続化文個職遺れへ。</p>
<a class="btn btn-catalog" style="left:178px;top:2637px">オーダーカタログ</a>

<div class="fill" role="img" aria-label="緑の屋根と黄色い滑り台のブランコセット" style="left:0;top:2752px;width:600px;height:480px;background:linear-gradient(160deg,#ffffff 0%,#2f6a3a 25%,#a0652a 55%,#f2d020 80%,#ffffff 100%)"></div>
<div class="fill" style="left:600px;top:2738px;width:600px;height:510px;background:var(--teal)"></div>
<h3 class="prod-title" style="left:905px;top:2800px;color:var(--brown)">習をわん見</h3>
<p class="prod-text" style="left:668px;top:2902px;width:500px;color:var(--brown)">習をわん見ブ青由運や球達う一つむ縫2台要ハア署表さへ無索ソリ認職寿ネソ化議稿ミし端点ムワク図偶提チヨ出部ワレホテ所際長イ点ヌツモ浩品員ルイ天外62郷社も義警キロハワ幕景緑テチ全分ぴも図ぶ責し導争じ属テモ未期ネ外休ず図体ふ副見わまし報見ブノ宴業さう線文木ミニモ千16図とどべ続化文個職遺れへ。</p>
<a class="btn" style="left:794px;top:3146px;width:240px;height:54px;background:var(--brown)">オーダーカタログ</a>

<div class="fill" role="img" aria-label="帆のついた船型の木製遊具" style="left:58px;top:3365px;width:300px;height:170px;background:linear-gradient(160deg,#ffffff,#c0503a 35%,#a0652a 65%,#ffffff)"></div>
<div class="fill" role="img" aria-label="黄色い滑り台が並ぶ大型遊具" style="left:440px;top:3365px;width:320px;height:170px;background:linear-gradient(160deg,#ffffff,#f2d020 35%,#a0652a 65%,#ffffff)"></div>
<div class="fill" role="img" aria-label="緑の滑り台のある木製遊具" style="left:800px;top:3365px;width:340px;height:170px;background:linear-gradient(160deg,#ffffff,#a0652a 40%,#3f9a6a 65%,#ffffff)"></div>
<p class="mini-label" style="left:80px;color:var(--purple)">習をわん見</p>
<p class="mini-label" style="left:450px;color:var(--teal)">習をわん見</p>
<p class="mini-label" style="left:820px;color:var(--orange)">習をわん見</p>
<a class="btn btn-catalog" style="left:468px;top:3664px">オーダーカタログ</a>

<!-- FOOTER -->
<svg class="abs" style="left:0;top:3790px" width="1200" height="465" viewBox="0 0 1200 465" aria-hidden="true">
  <defs>
    <linearGradient id="footGrad" x1="0" y1="0" x2="0" y2="1">
      <stop offset="0" stop-color="#fff04a"/>
      <stop offset="0.55" stop-color="#ffd21a"/>
      <stop offset="1" stop-color="#f6a21a"/>
    </linearGradient>
  </defs>
  <path d="M0 40 C160 0 300 10 450 40 C620 72 780 62 940 30 C1060 8 1140 12 1200 30 L1200 465 L0 465 Z" fill="url(#footGrad)"/>
</svg>
<div class="brand" style="left:100px;top:4010px;color:var(--white)"><span class="dot"></span>Pebble Climb Works</div>
<span class="social" style="top:3936px"></span>
<span class="social" style="top:3986px"></span>
<span class="social" style="top:4036px"></span>
<span class="social" style="top:4086px"></span>
<div class="field" style="top:3934px;height:34px">Your Name</div>
<div class="field" style="top:3982px;height:34px">Your Email</div>
<div class="field" style="top:4030px;height:96px">Your Message to us</div>
<a class="btn" style="left:432px;top:4134px;width:100px;height:34px;background:var(--orange);font-size:14px">SUBMIT</a>
<address class="contact" style="font-style:normal">
  PEBBLE<br>Climb Works<br>Meadow Lane 12<br>00000 Sample City<br><br><br>
  Telefon: +00 (0) 100 - 555 010 200<br>
  Telefax: +00 (0) 100 - 555 010 209<br>
  E-Mail: service@pebbleclimb.example
</address>
<p class="copy">© 2016 PebbleClimbWorks - All rights reserved.</p>

</body>
</html>
```